New business card for our new logo

I have a brand new, existing logo. Now I need it on a new business card. The new card should include the following:

English language training
Translations
Interpreting Services (remote and in-person)

Target Market(s)

We are targeting international companies with foreign investment in the United States as well as domestic companies, medical offices, law offices, and non-profits that have non-native English speakers as their clients.

Contact Information for Business Card

Marla Quennet, President
418 Garvin St.
Indianapolis, IN 46871
(317) 584-2316
info@brightpathwordworks.com
www.brightpathwordworks.com

Font styles to use
Sans Serif

Colors
0392cd
3176b5
abd036
9bcb3b
f04a50
f78f20

Requirements
Must have
• It must include our logo and business card details
Nice to have
• I would like to see a layout that is uncluttered and conveys trust and dependability, as well as the feelings of being friendly and approachable.

It would be nice to have icons for English language training, translating, and interpreting.
Should not have
• No pink, yellow, or purple

```html
<!DOCTYPE html>
<html lang="en">
<head>
<meta charset="utf-8">
<title>Brightpath Wordworks – Business Card</title>
<link rel="stylesheet" href="https://fonts.googleapis.com/css2?family=Montserrat:wght@400;500;600;700&display=swap">
<style>
  :root {
    --brand-blue: #2a78b7;
    --paper: #f7f7f6;
    --ink: #3a3a3a;
    --backdrop: #a0a0a0;
  }
  * { margin: 0; padding: 0; box-sizing: border-box; }
  html, body { width: 1021px; height: 1200px; overflow: hidden; }
  body {
    background: var(--backdrop);
    font-family: "Montserrat", Arial, sans-serif;
    position: relative;
  }
  .card {
    position: absolute;
    width: 753px;
    height: 429px;
  }
  .card-front { left: 134px; top: 119px; background: var(--brand-blue); }
  .card-back { left: 131px; top: 651px; background: var(--paper); color: var(--ink); }

  .front-mark {
    position: absolute;
    left: 119px; top: 115px;
    width: 196px; height: 196px;
    border-radius: 50%;
    background: #fff;
  }
  .front-name {
    position: absolute;
    left: 345px; top: 125px;
    color: #fff;
    font-weight: 600;
    font-size: 58px;
    line-height: 70px;
    letter-spacing: 0.5px;
  }

  .services { position: absolute; left: 36px; top: 57px; list-style: none; }
  .service {
    display: flex; align-items: center;
    height: 32px; margin-bottom: 11.5px;
    font-size: 18.5px; font-weight: 500; letter-spacing: 0.4px;
  }
  .service-icon { width: 32px; height: 32px; margin-right: 10px; flex: none; }

  .back-mark {
    position: absolute;
    left: 420px; top: 59px;
    width: 112px; height: 112px;
    border-radius: 50%;
    background: var(--brand-blue);
  }
  .back-name {
    position: absolute;
    left: 549px; top: 74px;
    color: var(--brand-blue);
    font-weight: 600;
    font-size: 32px;
    line-height: 40px;
  }

  .person-name {
    position: absolute; left: 36px; top: 236px;
    font-size: 30px; font-weight: 700; color: var(--brand-blue);
    letter-spacing: 0.3px;
  }
  .person-title {
    position: absolute; left: 36px; top: 273px;
    font-size: 17px; font-weight: 400;
  }
  .title-rule {
    position: absolute; left: 127px; top: 284px;
    width: 587px; height: 1px; background: var(--brand-blue);
  }

  .contact { position: absolute; left: 36px; top: 315px; list-style: none; }
  .contact-item {
    display: flex; align-items: center;
    height: 26px; font-size: 17.5px; font-weight: 400;
  }
  .contact-icon { width: 14px; height: 14px; margin-right: 5px; flex: none; }
  .domain { color: var(--brand-blue); }

  .address {
    position: absolute; left: 388px; top: 347px;
    border-left: 2px solid var(--brand-blue);
    padding-left: 13px;
    font-size: 17.5px; line-height: 22px; font-style: normal;
  }
</style>
</head>
<body>
  <section class="card card-front">
    <div class="front-mark"></div>
    <div class="front-name">Brightpath<br>Wordworks</div>
  </section>

  <section class="card card-back">
    <ul class="services">
      <li class="service">
        <svg class="service-icon" viewBox="0 0 32 32" fill="none" stroke="#2a78b7" stroke-width="1.3">
          <circle cx="16" cy="16" r="15"/>
          <path d="M7 9h10v7h-6l-3 3v-3H7z"/>
          <path d="M14 14h11v7h-2v3l-3-3h-6z"/>
        </svg>
        Translations
      </li>
      <li class="service">
        <svg class="service-icon" viewBox="0 0 32 32" fill="none" stroke="#2a78b7" stroke-width="1.3">
          <circle cx="16" cy="16" r="15"/>
          <rect x="8" y="8" width="16" height="10"/>
          <path d="M11 12h6M11 15h4M10 24v-4M22 24v-4M14 24h4"/>
        </svg>
        English language training
      </li>
      <li class="service">
        <svg class="service-icon" viewBox="0 0 32 32" fill="none" stroke="#2a78b7" stroke-width="1.3">
          <circle cx="16" cy="16" r="15"/>
          <path d="M10 11a6 6 0 0 1 12 0M9 11h3v6H9zM20 11h3v6h-3zM22 17v3h-5"/>
        </svg>
        Interpreting Services
      </li>
    </ul>

    <div class="back-mark"></div>
    <div class="back-name">Brightpath<br>Wordworks</div>

    <h1 class="person-name">MARLA QUENNET</h1>
    <p class="person-title">President</p>
    <div class="title-rule"></div>

    <ul class="contact">
      <li class="contact-item">
        <svg class="contact-icon" viewBox="0 0 16 16"><path fill="#2a78b7" d="M3 1l3 3-1.5 2a9 9 0 0 0 5.5 5.5L12 10l3 3-2 2C7 15 1 9 1 3z"/></svg>
        (317) 584-2316
      </li>
      <li class="contact-item">
        <svg class="contact-icon" viewBox="0 0 16 16"><path fill="#2a78b7" d="M1 3h14v10H1z"/><path fill="none" stroke="#f7f7f6" stroke-width="1.2" d="M1 3l7 6 7-6M1 13l5-5M15 13l-5-5"/></svg>
        info@brightpathwordworks.com
      </li>
      <li class="contact-item">
        <svg class="contact-icon" viewBox="0 0 16 16"><circle cx="8" cy="8" r="7" fill="#2a78b7"/><path fill="none" stroke="#f7f7f6" stroke-width="1.1" d="M1 8h14M8 1c-3 4-3 10 0 14M8 1c3 4 3 10 0 14"/></svg>
        <span>www.<span class="domain">brightpathwordworks</span>.com</span>
      </li>
    </ul>

    <address class="address">418 Garvin St.<br>Indianapolis, IN 46871</address>
  </section>
</body>
</html>
```